PL Dunmore Electric Yard Sign

Looking to have a yard sign designed that we can place at projects we are working on. Most likely will be 18" H x 24" W but flexible that we can increase the size if necessary. It should include our logo, our phone # 555-214-7796, website pldunmoreelectric.example and slogan, built on integrity, driven by excellence. Colors should match our brand.

```html
<!DOCTYPE html>
<html lang="en">
<head>
<meta charset="utf-8">
<title>PL Dunmore Electric Yard Sign</title>
<link rel="stylesheet" href="https://fonts.googleapis.com/css2?family=Saira+Semi+Condensed:wght@700;800&family=Ubuntu:wght@700&display=swap">
<style>
  :root {
    --navy: #2b3656;
    --red: #df2530;
    --white: #ffffff;
    --backdrop: #f1f1f1;
  }
  * { margin: 0; padding: 0; box-sizing: border-box; }
  html, body {
    width: 1200px;
    height: 411px;
    overflow: hidden;
    background: var(--backdrop);
  }
  .canvas {
    width: 1200px;
    height: 411px;
    display: flex;
    align-items: center;
    justify-content: center;
  }
  .yard-sign {
    width: 480px;
    height: 360px;
    background: var(--white);
    box-shadow: 0 6px 18px rgba(0,0,0,0.12);
    display: flex;
    flex-direction: column;
    align-items: center;
    position: relative;
  }
  .brand {
    margin-top: 86px;
    display: flex;
    align-items: center;
    gap: 10px;
  }
  .brand-mark {
    width: 16px;
    height: 16px;
    background: var(--red);
  }
  .brand-name {
    font-family: "Saira Semi Condensed", sans-serif;
    font-weight: 800;
    font-size: 44px;
    line-height: 1;
    letter-spacing: 3px;
    color: var(--red);
    text-transform: uppercase;
  }
  .trade {
    margin-top: 10px;
    font-family: "Ubuntu", sans-serif;
    font-weight: 700;
    font-size: 21px;
    letter-spacing: 4.6px;
    color: var(--navy);
    line-height: 1;
  }
  .trade-rule {
    margin-top: 5px;
    width: 436px;
    height: 3px;
    background: var(--red);
    border-bottom: 1px solid var(--navy);
  }
  .phone {
    margin-top: 10px;
    font-family: "Saira Semi Condensed", sans-serif;
    font-weight: 800;
    font-size: 62px;
    line-height: 1;
    color: var(--navy);
    letter-spacing: 1px;
  }
  .website {
    margin-top: 4px;
    font-family: "Ubuntu", sans-serif;
    font-weight: 700;
    font-size: 15px;
    letter-spacing: 3.2px;
    color: var(--navy);
  }
  .slogan-band {
    position: absolute;
    left: 0;
    right: 0;
    bottom: 0;
    height: 54px;
    display: flex;
    font-family: "Ubuntu", sans-serif;
    font-weight: 700;
    font-size: 19px;
    color: var(--white);
  }
  .slogan-band span {
    display: flex;
    align-items: center;
    justify-content: center;
  }
  .slogan-integrity { width: 225px; background: var(--navy); }
  .slogan-excellence { flex: 1; background: var(--red); }
</style>
</head>
<body>
  <main class="canvas">
    <section class="yard-sign" aria-label="PL Dunmore Electric yard sign">
      <div class="brand">
        <span class="brand-mark" aria-hidden="true"></span>
        <h1 class="brand-name">P.L. Dunmore</h1>
      </div>
      <p class="trade">Electrical Contractor</p>
      <div class="trade-rule" aria-hidden="true"></div>
      <p class="phone">555-214-7796</p>
      <p class="website">www.pldunmoreelectric.example</p>
      <div class="slogan-band">
        <span class="slogan-integrity">built on integrity</span>
        <span class="slogan-excellence">driven by excellence</span>
      </div>
    </section>
  </main>
</body>
</html>
```